Brindle.vc needs a better website design!

We need a new and better website for Brindle.vc. We're a Canadian venture capital firm that invests in innovative entrepreneurs. We compete against the following websites: tollery.vc, quorbinvest.ca, gavelvc.com, and duskara.vc. We're a diverse group of partners and we're dedicated to the founders we invest in.
Updates

I don’t really like stock photos of random people as part of the website design…so please try to stay away from using those images. Thanks, Owen

Target Market(s)

Canadian entrepreneurs and investors

Industry/Entity Type

Venture capital, finance, investment, entrepreneurship

Coding

Coded - Design and coding required

Number of Pages Required

4 page

Font styles to use
Sans Serif

Colors

Designer to choose colors to be used in the design.

Requirements
Must have
• Clean crisp overall design. Fast and to the point.
Nice to have
• Check out www.brindle.vc - I did it myself and it is too basic and too wordy.
Should not have
• No stock images with random people in them! Not too wordy or with too many large images that are slow to load.

```html
<!DOCTYPE html>
<html lang="en">
<head>
<meta charset="utf-8">
<title>Brindle.vc</title>
<link href="https://fonts.googleapis.com/css2?family=Poppins:wght@400;500;600;700&display=swap" rel="stylesheet">
<style>
:root{
  --green:#7a9a2e;
  --green-dark:#6b8a25;
  --ink:#1d1d1d;
  --muted:#444;
  --teal-a:#123f45;
  --teal-b:#0a6466;
  --gray-bg:#f3f3f3;
  --line:#dcdcdc;
  --black:#050505;
}
*{box-sizing:border-box;margin:0;padding:0}
html,body{width:1200px;height:2950px;overflow:hidden;background:#fff}
body{font-family:'Poppins',sans-serif;color:var(--ink);position:relative}
.abs{position:absolute}
.center{text-align:center}

/* header */
.site-header{position:absolute;left:0;top:0;width:1200px;height:56px;background:#fff;z-index:5}
.brand{position:absolute;left:88px;top:0;width:136px;height:120px;background:#fff;border-left:5px solid var(--green);z-index:6;display:flex;flex-direction:column;align-items:center;justify-content:center;gap:8px}
.brand-dot{width:44px;height:44px;border-radius:50%;background:var(--green)}
.brand-name{font-size:18px;font-weight:600;color:var(--green);letter-spacing:.5px}
.main-nav{position:absolute;top:17px;left:0;width:100%;font-size:15px}
.main-nav a{position:absolute;color:var(--ink);text-decoration:none}
.main-nav a.active{color:var(--green);border-bottom:1px solid var(--green);padding-bottom:2px}
.btn-inquiry{position:absolute;left:978px;top:11px;width:133px;height:34px;background:var(--green);color:#fff;font-size:15px;font-weight:600;display:flex;align-items:center;justify-content:center;border-radius:2px}

/* hero */
.hero{position:absolute;left:0;top:56px;width:1200px;height:450px;background:linear-gradient(180deg,#1b2128 0%,#2b333b 45%,#1e2a33 100%)}
.hero-title{position:absolute;top:206px;width:100%;color:#fff;font-size:34px;font-weight:600}
.hero-text{position:absolute;top:255px;width:100%;color:#fff;font-size:18px;line-height:24px}

.section-title{position:absolute;width:100%;color:var(--green);font-size:30px;font-weight:600;line-height:32px;text-align:center}

/* characteristics */
.trait{position:absolute;top:710px;width:244px;height:92px;border:1px solid var(--line);background:#fff}
.trait-icon{position:absolute;left:85px;top:-36px;width:74px;height:74px;border-radius:50%;background:var(--green);display:flex;align-items:center;justify-content:center}
.trait-label{position:absolute;bottom:20px;width:100%;text-align:center;font-size:16px;font-weight:600}

/* considerations */
.consider{position:absolute;left:0;top:882px;width:1200px;height:440px;background:linear-gradient(120deg,var(--teal-a) 0%,#0d5558 50%,var(--teal-b) 100%)}
.consider-title{color:#fff;top:975px}
.consider-panel{position:absolute;left:139px;top:1065px;width:922px;height:346px;background:#fff;box-shadow:0 4px 14px rgba(0,0,0,.08);z-index:3}
.factor{position:absolute;width:270px;height:80px}
.factor-icon{position:absolute;left:0;top:0;width:64px;height:64px;border-radius:50%;background:var(--green);display:flex;align-items:center;justify-content:center}
.factor-body{position:absolute;left:72px;top:-6px;width:182px;font-size:13px;line-height:17.5px;color:var(--ink)}
.factor-body strong{display:block;color:var(--green);font-size:15px;font-weight:600;margin-bottom:1px;white-space:nowrap}
.btn-outline{position:absolute;left:405px;top:277px;width:112px;height:32px;border:1px solid #9a9a9a;border-radius:2px;font-size:15px;display:flex;align-items:center;justify-content:center}

/* team */
.team{position:absolute;left:0;top:1322px;width:1200px;height:524px;background:var(--gray-bg)}
.member{position:absolute;top:1553px;width:192px}
.member-photo{width:192px;height:199px;background:linear-gradient(180deg,#fafafa 0%,#e7dfd6 60%,#3b342f 100%);box-shadow:0 2px 6px rgba(0,0,0,.12)}
.member-name{margin-top:16px;font-size:17px;text-align:center}
.arrow-btn{position:absolute;width:28px;height:28px;border:1.5px solid var(--ink);border-radius:7px;display:flex;align-items:center;justify-content:center;background:#fff}
.arrow-btn.on{border-color:var(--green)}

/* companies */
.company{position:absolute;top:1989px;width:228px;height:102px;border:1px solid var(--line);background:#fff;display:flex;flex-direction:column;align-items:center;justify-content:center;gap:2px}
.company-name{font-size:34px;font-weight:700;color:#2a2a2a;line-height:38px}
.company-tag{font-size:13px;color:#2a2a2a}

/* inquiry */
.inquiry{position:absolute;left:0;top:2244px;width:1200px;height:520px;background:radial-gradient(ellipse at 50% 40%,#f7f7f7 0%,#ececec 45%,#bdbdbd 100%)}
.field{position:absolute;background:#fff;border:1px solid var(--line);font-size:10px;color:#888;padding:14px 15px}
.btn-submit{position:absolute;left:552px;top:2584px;width:98px;height:33px;background:var(--green);color:#fff;font-size:15px;font-weight:500;display:flex;align-items:center;justify-content:center;border-radius:2px}

/* footer */
.site-footer{position:absolute;left:0;top:2748px;width:1200px;height:162px;background:var(--black)}
.contact{position:absolute;top:2782px;display:flex;align-items:center;gap:14px;color:#fff;font-size:14px;line-height:20px}
.contact-icon{width:46px;height:46px;border-radius:50%;background:var(--green);display:flex;align-items:center;justify-content:center;flex:none}
.footer-nav a{position:absolute;top:2857px;color:#fff;font-size:14px;text-decoration:none}
.footer-nav a.active{color:var(--green);border-bottom:1px solid var(--green)}
.bottom-bar{position:absolute;left:0;top:2910px;width:1200px;height:40px;background:var(--green-dark)}
.copyright{position:absolute;left:89px;top:11px;font-size:13px;color:#1d1d1d}
.social{position:absolute;top:14px;width:12px;height:12px;border-radius:50%;background:#1d1d1d}
</style>
</head>
<body>

<header class="site-header">
  <nav class="main-nav">
    <a class="active" style="left:545px">Home</a>
    <a style="left:624px">Team</a>
    <a style="left:701px">Companies</a>
    <a style="left:820px">What We Look For</a>
  </nav>
  <div class="btn-inquiry">Quick Inquiry</div>
</header>
<div class="brand"><span class="brand-dot"></span><span class="brand-name">BRINDLE.VC</span></div>

<section class="hero" role="img" aria-label="Dusk city skyline with a tall observation tower">
</section>
<h1 class="hero-title center abs" style="top:206px">Brindle.vc</h1>
<p class="hero-text center abs">is a venture capital firm that invests in innovative seed-stage technology<br>companies in Western Canada focused on B2B and SaaS markets.</p>
<svg class="abs" style="left:0;top:420px" width="1200" height="90" viewBox="0 0 1200 90">
  <polygon points="0,4 600,80 1200,4 1200,90 0,90" fill="#fff"/>
  <polygon points="280,40 600,80 920,40 600,68" fill="var(--green)"/>
</svg>

<h2 class="section-title" style="top:575px">We invest in innovative technology companies<br>with these characteristics:</h2>

<div class="trait" style="left:204px">
  <div class="trait-icon"><svg width="40" height="40" viewBox="0 0 40 40" fill="none" stroke="#fff" stroke-width="2"><rect x="9" y="9" width="22" height="22" rx="4" transform="rotate(45 20 20)"/><circle cx="20" cy="20" r="5"/></svg></div>
  <div class="trait-label">Founding Team</div>
</div>
<div class="trait" style="left:472px">
  <div class="trait-icon"><svg width="40" height="40" viewBox="0 0 40 40" fill="none" stroke="#fff" stroke-width="2"><path d="M6 34h28M9 34V22M16 34V16M23 34V20M30 34V12M8 18l8-8 7 6 9-9"/></svg></div>
  <div class="trait-label">Total Addressable Market</div>
</div>
<div class="trait" style="left:740px">
  <div class="trait-icon"><svg width="40" height="40" viewBox="0 0 40 40" fill="none" stroke="#fff" stroke-width="2"><rect x="7" y="20" width="26" height="14"/><path d="M7 20l5-6h16l5 6M20 20v14"/><circle cx="20" cy="9" r="4"/></svg></div>
  <div class="trait-label">Product Market Fit</div>
</div>

<section class="consider" role="img" aria-label="Teal tinted city skyline with observation tower"></section>
<h2 class="section-title consider-title">Other things we consider in evaluating our<br>venture capital investments:</h2>

<section class="team"></section>

<div class="consider-panel">
  <div class="factor" style="left:38px;top:52px">
    <div class="factor-icon"><svg width="38" height="38" viewBox="0 0 38 38" fill="none" stroke="#fff" stroke-width="2"><circle cx="19" cy="19" r="14"/><path d="M19 11v8l6 4"/></svg></div>
    <div class="factor-body"><strong>Timing:</strong>Supportive Market Trends; Not Too Early or Too Late, Just Right</div>
  </div>
  <div class="factor" style="left:325px;top:52px">
    <div class="factor-icon"><svg width="38" height="38" viewBox="0 0 38 38" fill="none" stroke="#fff" stroke-width="2"><circle cx="12" cy="12" r="4"/><circle cx="26" cy="12" r="4"/><path d="M5 26c0-5 4-8 7-8s7 3 7 8M19 26c0-5 4-8 7-8s7 3 7 8M4 32h30"/></svg></div>
    <div class="factor-body"><strong>Customers:</strong>Understand Who + How to Reach; Realistic Go to Market Strategy</div>
  </div>
  <div class="factor" style="left:617px;top:52px">
    <div class="factor-icon"><svg width="38" height="38" viewBox="0 0 38 38" fill="none" stroke="#fff" stroke-width="2"><path d="M5 33h28M8 33V20h7v13M16 33V14h7v19M24 33V22h7v11"/><circle cx="19" cy="7" r="3"/></svg></div>
    <div class="factor-body"><strong>Competitive Advantage:</strong>Secret Sauce / Protective Moat for Product or Technology</div>
  </div>
  <div class="factor" style="left:38px;top:168px">
    <div class="factor-icon"><svg width="38" height="38" viewBox="0 0 38 38" fill="none" stroke="#fff" stroke-width="2"><path d="M19 5L34 32H4z"/><path d="M19 14v10M19 27v2"/></svg></div>
    <div class="factor-body"><strong>Problem:</strong>Big Pain; Customers Care About It + Are Willing to Pay</div>
  </div>
  <div class="factor" style="left:325px;top:168px">
    <div class="factor-icon"><svg width="38" height="38" viewBox="0 0 38 38" fill="none" stroke="#fff" stroke-width="2"><rect x="15" y="4" width="8" height="7"/><rect x="4" y="27" width="8" height="7"/><rect x="26" y="27" width="8" height="7"/><rect x="15" y="16" width="8" height="6"/><path d="M19 11v5M19 22v2M8 27v-3h22v3"/></svg></div>
    <div class="factor-body"><strong>Business Model:</strong>Clear + Compelling; Increasing Scale Returns; Realizable Projections</div>
  </div>
  <div class="factor" style="left:617px;top:168px">
    <div class="factor-icon"><svg width="38" height="38" viewBox="0 0 38 38" fill="none" stroke="#fff" stroke-width="2"><circle cx="20" cy="15" r="10"/><path d="M23 11h-4a2 2 0 0 0 0 4h2a2 2 0 0 1 0 4h-4M20 9v2M20 19v2M4 30l6-4h8l8 3"/></svg></div>
    <div class="factor-body"><strong>Funding:</strong>Smart Use; Enough to Reach Milestones; Series A Potential; Exit Opportunities</div>
  </div>
  <div class="btn-outline">View All</div>
</div>

<h2 class="section-title" style="top:1486px">Our Teams</h2>
<div class="arrow-btn" style="left:112px;top:1638px"><svg width="14" height="14" viewBox="0 0 14 14" fill="none" stroke="#1d1d1d" stroke-width="1.6"><path d="M12 7H2M6 3L2 7l4 4"/></svg></div>
<div class="arrow-btn on" style="left:1060px;top:1638px"><svg width="14" height="14" viewBox="0 0 14 14" fill="none" stroke="#7a9a2e" stroke-width="1.6"><path d="M2 7h10M8 3l4 4-4 4"/></svg></div>
<div class="member" style="left:180px"><div class="member-photo" role="img" aria-label="Illustrated portrait of Owen Halvik"></div><div class="member-name">Owen Halvik</div></div>
<div class="member" style="left:396px"><div class="member-photo" role="img" aria-label="Illustrated portrait of Devan Ashar"></div><div class="member-name">Devan Ashar</div></div>
<div class="member" style="left:612px"><div class="member-photo" role="img" aria-label="Illustrated portrait of Marta Celling"></div><div class="member-name">Marta Celling</div></div>
<div class="member" style="left:828px"><div class="member-photo" role="img" aria-label="Illustrated portrait of Corey Wynd"></div><div class="member-name">Corey Wynd</div></div>

<h2 class="section-title" style="top:1921px">Our Companies</h2>
<div class="company" style="left:105px"><span class="company-name">tallyrun</span></div>
<div class="company" style="left:358px"><span class="company-name">Quilops</span></div>
<div class="company" style="left:612px"><span class="company-name">nutrivault</span><span class="company-tag">Blended For You</span></div>
<div class="company" style="left:866px"><span class="company-name" style="font-weight:400">Veyra</span></div>
<div class="arrow-btn" style="left:568px;top:2131px"><svg width="14" height="14" viewBox="0 0 14 14" fill="none" stroke="#1d1d1d" stroke-width="1.6"><path d="M12 7H2M6 3L2 7l4 4"/></svg></div>
<div class="arrow-btn on" style="left:604px;top:2131px"><svg width="14" height="14" viewBox="0 0 14 14" fill="none" stroke="#7a9a2e" stroke-width="1.6"><path d="M2 7h10M8 3l4 4-4 4"/></svg></div>

<section class="inquiry" role="img" aria-label="Faded greyscale office meeting scene"></section>
<h2 class="section-title" style="top:2316px">Quick Inquiry</h2>
<div class="field" style="left:229px;top:2387px;width:362px;height:38px;padding-top:13px">Full Name</div>
<div class="field" style="left:229px;top:2439px;width:362px;height:40px">Email*</div>
<div class="field" style="left:229px;top:2493px;width:362px;height:40px">Phone</div>
<div class="field" style="left:609px;top:2387px;width:362px;height:146px;padding-top:13px">Have questions? We have answers!*</div>
<div class="btn-submit">Submit</div>

<svg class="abs" style="left:0;top:2690px" width="1200" height="62" viewBox="0 0 1200 62">
  <polygon points="0,58 600,10 1200,58 1200,62 0,62" fill="var(--black)"/>
  <polygon points="360,34 600,0 840,34 600,14" fill="var(--green)"/>
</svg>
<footer class="site-footer"></footer>
<div class="contact" style="left:248px">
  <span class="contact-icon"><svg width="20" height="20" viewBox="0 0 20 20" fill="#fff"><path d="M10 1a6 6 0 0 0-6 6c0 5 6 12 6 12s6-7 6-12a6 6 0 0 0-6-6zm0 8.5A2.5 2.5 0 1 1 10 4.5a2.5 2.5 0 0 1 0 5z"/></svg></span>
  <span>Aldermoor Weg 12<br>40210 Lindenfeld Germany</span>
</div>
<div class="contact" style="left:555px">
  <span class="contact-icon"><svg width="18" height="18" viewBox="0 0 20 20" fill="#fff"><path d="M5 2l3 4-2 2c1 2 4 5 6 6l2-2 4 3-2 3C9 18 2 11 2 4z"/></svg></span>
  <span>+49-170-5521904</span>
</div>
<div class="contact" style="left:791px">
  <span class="contact-icon"><svg width="20" height="16" viewBox="0 0 20 16" fill="#fff"><path d="M1 2h18v12H1z" fill="none" stroke="#fff" stroke-width="1.6"/><path d="M1 2l9 7 9-7" fill="none" stroke="#fff" stroke-width="1.6"/></svg></span>
  <span>info@brindle.vc</span>
</div>
<nav class="footer-nav">
  <a class="active" style="left:409px">Home</a>
  <a style="left:479px">Team</a>
  <a style="left:547px">Companies</a>
  <a style="left:653px">What We Look For</a>
</nav>
<div class="bottom-bar">
  <span class="copyright">Copyright © 2021 Brindle. All Rights Reserved</span>
  <span class="social" style="left:1004px"></span>
  <span class="social" style="left:1034px"></span>
  <span class="social" style="left:1065px"></span>
  <span class="social" style="left:1098px"></span>
</div>

</body>
</html>
```